Wedding Company needs Brochure Design

FOR THIS PROJECT, WE ARE LOOKING FOR A BROCHURE. WHOEVER WE CHOOSE AS THE WINNING BROCHURE DESIGN WILL THEN DESIGN OUR WEBSITE AND BUSINESS CARD.

We're are looking to expand our brochure by making it a circle and adding 6 inside pages of information with a front and back cover. The pages will be as follows:

Front
About us
About us pictures
Wedding Planning
Wedding planning pictures
Lighting & Decor
Lighting & decor pictures
Back

We've uploaded a picture of our current brochure... so you can get an idea of what we've liked before. Please give us your creative input & design ideas. We've put together a "mock" brochure for you to take a look at as well. As you can see we need your help to properly lay out pictures so that the pages look full and the pictures pop and catches our clients attention.

A few words to describe our brochure would be "elegance", "class", "tasteful" and "colorful". We want to be able to portray that we are luxurious and innovative for the higher end brides and at the same time catering to the budget friendly brides.

Currently, we are waiting on a few pictures from the photographers and we are hoping to have them in a few days... In the meantime we've placed pictures we took from our phone as place holders.

```html
<!DOCTYPE html>
<html lang="en">
<head>
<meta charset="utf-8">
<title>Lighting &amp; Decor – Brochure Spread</title>
<link rel="stylesheet" href="https://fonts.googleapis.com/css2?family=Indie+Flower&family=Dancing+Script:wght@700&display=swap">
<style>
  :root {
    --backdrop: #3d4144;
    --ring-light: #d3d5d6;
    --ring-mid: #b9bcbe;
    --stitch: #8f9396;
    --rim-white: #ffffff;
    --page-fill: #dcdddd;
    --page-fill-deep: #cfd1d1;
    --ink: #6a6d6f;
    --ink-soft: #7b7e80;
  }
  html, body {
    margin: 0;
    padding: 0;
    overflow: hidden;
    background: var(--backdrop);
  }
  .spread {
    position: relative;
    width: 1200px;
    height: 583px;
    background: var(--backdrop);
    overflow: hidden;
  }
  .spread-art {
    position: absolute;
    inset: 0;
  }
  .page-copy {
    position: absolute;
    left: 106px;
    top: 100px;
    width: 480px;
    text-align: center;
    color: var(--ink);
  }
  .page-title {
    margin: 0;
    font-family: "Indie Flower", cursive;
    font-weight: 400;
    font-size: 38px;
    line-height: 1;
    color: var(--ink-soft);
    letter-spacing: 0.5px;
  }
  .page-intro {
    margin: 52px 0 0;
    font-family: "Dancing Script", cursive;
    font-weight: 700;
    font-size: 10px;
    line-height: 12.6px;
    color: var(--ink);
  }
  .service-list {
    display: flex;
    justify-content: center;
    gap: 40px;
    margin-top: 22px;
    font-family: "Dancing Script", cursive;
    font-weight: 700;
    font-size: 10.5px;
    line-height: 16.4px;
    color: var(--ink);
  }
  .service-list ul {
    list-style: none;
    margin: 0;
    padding: 0;
    width: 120px;
  }
  .service-list .services-core { text-align: right; }
  .service-list .services-extra { text-align: left; }
</style>
</head>
<body>
<main class="spread">
  <svg class="spread-art" width="1200" height="583" viewBox="0 0 1200 583" xmlns="http://www.w3.org/2000/svg">
    <defs>
      <radialGradient id="ring-tone" cx="50%" cy="45%" r="55%">
        <stop offset="0.85" stop-color="#c4c7c8"/>
        <stop offset="0.93" stop-color="#d7d9da"/>
        <stop offset="1" stop-color="#b5b8ba"/>
      </radialGradient>
      <linearGradient id="page-tone" x1="0" y1="0" x2="1" y2="1">
        <stop offset="0" stop-color="#e3e4e4"/>
        <stop offset="1" stop-color="#d2d3d3"/>
      </linearGradient>
      <clipPath id="collage-clip">
        <circle cx="873" cy="290" r="240"/>
      </clipPath>
      <linearGradient id="tone-crowd" x1="0" y1="0" x2="1" y2="1">
        <stop offset="0" stop-color="#4a2f5e"/>
        <stop offset="0.5" stop-color="#1f1a26"/>
        <stop offset="1" stop-color="#5a3f6a"/>
      </linearGradient>
      <linearGradient id="tone-tent" x1="0" y1="0" x2="1" y2="1">
        <stop offset="0" stop-color="#8b3be0"/>
        <stop offset="0.55" stop-color="#3f3fd4"/>
        <stop offset="1" stop-color="#c04fb8"/>
      </linearGradient>
      <linearGradient id="tone-confetti" x1="0" y1="0" x2="1" y2="1">
        <stop offset="0" stop-color="#7a2c1c"/>
        <stop offset="0.5" stop-color="#b4452f"/>
        <stop offset="1" stop-color="#8a4a3a"/>
      </linearGradient>
      <linearGradient id="tone-reception" x1="0" y1="0" x2="1" y2="0">
        <stop offset="0" stop-color="#b83fd0"/>
        <stop offset="0.5" stop-color="#2fa2b8"/>
        <stop offset="1" stop-color="#d04a9a"/>
      </linearGradient>
      <linearGradient id="tone-monogram" x1="0" y1="0" x2="0" y2="1">
        <stop offset="0" stop-color="#f6f4f4"/>
        <stop offset="1" stop-color="#e4e1e2"/>
      </linearGradient>
    </defs>

    <!-- Left page: text page -->
    <g class="page page-text">
      <circle class="page-ring" cx="346" cy="290" r="268" fill="url(#ring-tone)"/>
      <circle class="page-stitch" cx="346" cy="290" r="259" fill="none" stroke="var(--stitch)" stroke-width="1" stroke-dasharray="2 3"/>
      <circle class="page-rim" cx="346" cy="290" r="252" fill="var(--rim-white)"/>
      <circle class="page-face" cx="346" cy="290" r="241" fill="url(#page-tone)"/>
    </g>

    <!-- Right page: photo collage -->
    <g class="page page-collage">
      <circle class="page-ring" cx="873" cy="290" r="268" fill="url(#ring-tone)"/>
      <circle class="page-stitch" cx="873" cy="290" r="259" fill="none" stroke="var(--stitch)" stroke-width="1" stroke-dasharray="2 3"/>
      <circle class="page-rim" cx="873" cy="290" r="252" fill="var(--rim-white)"/>
      <g class="collage" clip-path="url(#collage-clip)">
        <rect x="600" y="40" width="546" height="500" fill="var(--rim-white)"/>
        <rect class="photo" role="img" aria-label="Photo of a large group of guests dressed in black posing together at an event" x="610" y="40" width="520" height="118" fill="url(#tone-crowd)"/>
        <rect class="photo" role="img" aria-label="Photo of a purple and blue lit draped ceremony tent with a crystal chandelier and floral arch" x="610" y="162" width="181" height="216" fill="url(#tone-tent)"/>
        <rect class="photo" role="img" aria-label="Photo of costumed performers and a guest celebrating under falling confetti" x="801" y="162" width="330" height="216" fill="url(#tone-confetti)"/>
        <rect class="photo" role="img" aria-label="Photo of a reception tent washed in magenta and teal uplighting with dining tables" x="640" y="384" width="313" height="160" fill="url(#tone-reception)"/>
        <rect class="photo" role="img" aria-label="Photo of a white monogram sign with the couple's initials and wedding date" x="960" y="384" width="170" height="124" fill="url(#tone-monogram)"/>
      </g>
    </g>
  </svg>

  <section class="page-copy">
    <h1 class="page-title">Lighting &amp; Decor</h1>
    <p class="page-intro">
      Let our experts demonstrate to your comfy dream centerpieces, surround your guests with<br>
      your event colors and romanticize your hotel in light. Looking for something romantic?<br>
      Imagine dining under lanterns and chandeliers. Ready to transform your event to a hot dance<br>
      club? Let our experts swirl and strobe light over your guests and dancefloor.<br>
      We offer a wide range of lighting services including, but not limited to:
    </p>
    <div class="service-list">
      <ul class="services-core">
        <li>- Pinspots -</li>
        <li>- Initial Monogram Lighting -</li>
        <li>- Uplighting -</li>
        <li>- Specials -</li>
        <li>- Dance Floors -</li>
        <li>- Draping -</li>
        <li>- Café Lights -</li>
      </ul>
      <ul class="services-extra">
        <li>Staging</li>
        <li>Search Lights</li>
        <li>Vinyl</li>
        <li>Video Projection</li>
        <li>Monograms</li>
        <li>Chiavari Chairs</li>
        <li>Custom Designs</li>
      </ul>
    </div>
  </section>
</main>
</body>
</html>
```